BUSINESS CARD needed for TRAVEL BUSINESS

-Background-

Wandorvist Crew (WC) is a newly found company in Asia that trains and develops people with various demographics to become a FREQUENT TRAVELER & an ENTREPRENEUR combined. Basically, the core product that the company markets teaches people how to TRAVEL leisurely and yet EARN MONEY at the same time. Our main quote will be LIVING LIFE BY LIVING.

- The Job -

We will be constantly going out to different events, whether opening promotional booths in roadshows or at colleges or going for networking events. Thus we need a BUSINESS CARD design that portrays our POSITIONING & BRANDING

- Positioning -

TRAVEL LEISURELY & EARN at the SAME TIME

- Objective -

Serve as a BTL marketing & networking tool

- Target Audience -

Male & Females aged 19 - 35 who LOVES to TRAVEL & have strong aspirations to make it big and attaining financial freedom. The audience are enthusiastic and when they see an opportunity, they will seize it on the very spot. They are well connected and have a wide social network.

- Single Minded Proposition -

WC is My Dream Life

Target Market(s)

REFER TO CREATIVE BRIEF

Industry/Entity Type

Marketing

Requirements
Must have
• 1) The business card must portray a branding thats related to TRAVEL.

Boarding pass design was what we came up with but express your creativity and surprise me with better ideas. :)
Nice to have
• This is an idea that we have and we would most likely like to use however I do not want to restrict your creativity so i am putting in NICE TO HAVE instead.

Our idea design -> To have the namecard in the format of a BOARDING PASS lookalike

(You may refer to these weblink for inspiration -> https://www.pictofind.example/search?hl=en&q=boarding+pass&bav=on.2,or.r_gc.r_pw.r_cp.r_qf.,cf.osb&biw=1366&bih=667&um=1&ie=UTF-8&tbm=isch&source=og&sa=N&tab=wi&ei=l-f9T4KqC4fWrQfx8eC-Bg

or simply PICTOFIND BOARDING PASS IMAGES

```html
<!DOCTYPE html>
<html lang="en">
<head>
<meta charset="UTF-8">
<title>Wandorvist Crew – Business Card</title>
<link rel="stylesheet" href="https://fonts.googleapis.com/css2?family=Oswald:wght@200;300&family=Roboto+Condensed:wght@300;700&display=swap">
<style>
  :root {
    --bg-centre: #3b4250;
    --bg-mid: #262b35;
    --bg-edge: #0e1116;
    --ink: #ffffff;
    --photo-frame: #d9dce1;
    --photo-sunset: #e3773c;
    --photo-dusk: #5a4f78;
    --photo-city: #2b4a72;
  }
  html, body {
    margin: 0;
    padding: 0;
    overflow: hidden;
  }
  body {
    width: 686px;
    height: 1200px;
    background: var(--bg-edge);
  }
  .card {
    position: relative;
    width: 686px;
    height: 1200px;
    overflow: hidden;
    background: radial-gradient(ellipse 75% 60% at 50% 48%, var(--bg-centre) 0%, var(--bg-mid) 55%, var(--bg-edge) 100%);
    color: var(--ink);
  }
  .tagline {
    position: absolute;
    top: 82px;
    left: 0;
    width: 100%;
    margin: 0;
    text-align: center;
    font-family: "Oswald", sans-serif;
    font-weight: 200;
    font-size: 96px;
    line-height: 1;
    white-space: nowrap;
    transform: scaleX(0.76);
    transform-origin: 50% 0;
  }
  .window-photo {
    position: absolute;
    left: 98px;
    top: 256px;
    width: 490px;
    height: 660px;
    border-radius: 160px;
    background: linear-gradient(180deg, var(--photo-frame) 0%, var(--photo-sunset) 22%, var(--photo-dusk) 38%, var(--photo-city) 62%, var(--photo-frame) 100%);
  }
  .contact {
    position: absolute;
    top: 1014px;
    left: 0;
    width: 100%;
    text-align: center;
    font-family: "Roboto Condensed", sans-serif;
    font-size: 32px;
    line-height: 53px;
  }
  .contact p {
    margin: 0;
  }
  .contact .label {
    font-weight: 700;
  }
  .contact .value {
    font-weight: 300;
  }
</style>
</head>
<body>
  <div class="card">
    <h1 class="tagline">LIVING LIFE BY LIVING</h1>

    <div class="window-photo" role="img" aria-label="Photograph of an aircraft window looking out on a city skyline with a tall iron tower over a lit river at sunset"></div>

    <div class="contact">
      <p><span class="label">Wandorvist:</span> <span class="value">Dorian Vale</span></p>
      <p><span class="label">Tel:</span> <span class="value">001 987 6543</span></p>
      <p><span class="label">Email</span> <span class="value">dorian@wandorvist.example</span></p>
    </div>
  </div>
</body>
</html>
```